Metal Fabrication Business Official Opening Party Invitation

We need a postcard designed to promote the official opening celebration of our business.

Dimensions can be:
148mm x 105mm OR 210 x 148mm
Flat card please - not folded - CAN be double sided if that suits your design better

We are a metal fabrication business which designs, engineers, repairs and manufactures a range of custom, quality metal works including vehicle trays, agricultural machinery implements, trailers, wood splitters, fire pits, furniture etc.
The brand position focuses on custom work of the highest quality.
The design for this piece should be INDUSTRIAL, (prefer a darker perhaps metal background) whilst still being fun and semi rustic. It's a party after all - but a party about metal. It will be winter so it's OK to have a "cold" feel - one of our products are firepits.

If you have questions or would like more specific information please ask.

Branding guidelines are attached. Feel free to go outside of these guidelines to add more creativity and fun to this particular design

Also attached some invited we found online that we like some parts of - VERY open to ideas and creativity, just as a bit of an idea what we like :) We'd LOVE something original and creative.
Updates

Target Market(s)

Males aged 30 - 60yrs
Country area - farmers and tradespeople

Industry/Entity Type

Business

Requirements
Must have
• Must be a unique, industrial (steel/metal) theme.
• Can include things like cogs/gears, screws etc in the design.
• see the attached 'invite likes..." also
• Text to be included in design include:
• Harrow Ironworks (can just use logo) official opening
• Date: Fri Aug 26
• Location: 5678 Road title
• Time: 6:00pm
• "Join us to celebrate the official opening of Harrow Ironworks"
• Light dinner provided
Should not have
• NO SHINY METAL FINISHES PLEASE

```html
<!DOCTYPE html>
<html lang="en">
<head>
<meta charset="utf-8">
<title>Harrow Ironworks – Official Opening Invitation</title>
<link rel="stylesheet" href="https://fonts.googleapis.com/css2?family=Orbitron:wght@700&family=Fira+Sans:wght@400&display=swap">
<style>
  :root {
    --stage-light: #d2d3d5;
    --stage-mid: #b4b5b8;
    --stage-dark: #9c9da0;
    --card-black: #1e1e1e;
    --ring-dark: #262626;
    --steel-grey: #a7a7a7;
    --brand-green: #6abf45;
    --accent-teal: #2ba4b9;
    --gear-navy: #1d3a66;
    --ink-white: #ffffff;
    --banner-blue: #0a3f8f;
    --banner-cyan: #0b8fd0;
  }
  * { margin: 0; padding: 0; box-sizing: border-box; }
  html, body { width: 1200px; height: 1000px; overflow: hidden; }
  body {
    position: relative;
    background: linear-gradient(160deg, var(--stage-light) 0%, var(--stage-mid) 45%, var(--stage-dark) 100%);
    font-family: "Fira Sans", sans-serif;
  }

  /* Front of card */
  .card-front {
    position: absolute; left: 0; top: 0; width: 736px; height: 520px;
    overflow: hidden; background: #2a2a2a;
  }
  .card-front svg { position: absolute; inset: 0; }
  .front-name {
    position: absolute; left: 0; width: 736px; text-align: center;
    font-family: "Orbitron", sans-serif; font-weight: 700;
    color: var(--steel-grey); letter-spacing: 4px;
  }
  .front-name.primary { top: 292px; font-size: 76px; }
  .front-name.secondary { top: 382px; font-size: 36px; letter-spacing: 8px; }

  /* Back of card */
  .card-back {
    position: absolute; left: 518px; top: 520px; width: 682px; height: 480px;
    background: var(--card-black); overflow: hidden;
  }
  .card-back svg.decor { position: absolute; inset: 0; }
  .back-brand {
    position: absolute; left: 54px; top: 136px;
    display: flex; align-items: center; gap: 16px;
  }
  .brand-square { width: 62px; height: 62px; background: var(--steel-grey); }
  .brand-name {
    font-family: "Orbitron", sans-serif; font-weight: 700;
    font-size: 33px; line-height: 1.1; color: var(--steel-grey); letter-spacing: 2px;
  }
  .invite-heading {
    position: absolute; left: 150px; top: 228px; width: 350px; height: 40px;
    display: flex; align-items: center; justify-content: space-between;
  }
  .invite-heading h1 {
    font-family: "Orbitron", sans-serif; font-weight: 700;
    font-size: 27px; color: var(--ink-white); letter-spacing: 2px;
  }
  .arrow { width: 0; height: 0; border-top: 11px solid transparent; border-bottom: 11px solid transparent; }
  .arrow.left { border-right: 54px solid var(--brand-green); }
  .arrow.right { border-left: 54px solid var(--brand-green); }
  .event-details {
    position: absolute; left: 202px; top: 288px; list-style: none;
    color: var(--ink-white); font-size: 17px; line-height: 24px;
  }
  .event-details li { padding-left: 14px; text-indent: -14px; }
</style>
</head>
<body>

<section class="card-front">
  <svg width="736" height="520" viewBox="0 0 736 520">
    <defs>
      <linearGradient id="bannerGrad" x1="0" y1="0" x2="1" y2="0">
        <stop offset="0" stop-color="var(--banner-blue)"/>
        <stop offset="1" stop-color="var(--banner-cyan)"/>
      </linearGradient>
      <radialGradient id="forgeGrad" cx="0.42" cy="0.58" r="0.7">
        <stop offset="0" stop-color="#7a4a26"/>
        <stop offset="0.35" stop-color="#3a3330"/>
        <stop offset="1" stop-color="#141414"/>
      </radialGradient>
      <linearGradient id="floorGrad" x1="0" y1="0" x2="1" y2="0">
        <stop offset="0" stop-color="#8d8d8d"/>
        <stop offset="0.5" stop-color="#3a3a3a"/>
        <stop offset="1" stop-color="#1a1a1a"/>
      </linearGradient>
    </defs>
    <rect width="736" height="520" fill="url(#floorGrad)"/>
    <path d="M0 0 H736 V72 Q520 40 300 52 Q120 62 0 120 Z" fill="url(#bannerGrad)"/>
    <path role="img" aria-label="Photo of a blacksmith hammering glowing hot steel on an anvil"
          d="M0 120 Q120 62 300 52 Q520 40 736 72 V410 Q560 450 380 440 Q180 430 0 420 Z"
          fill="url(#forgeGrad)"/>
  </svg>
  <div class="front-name primary">HARROW</div>
  <div class="front-name secondary">IRONWORKS</div>
</section>

<section class="card-back">
  <svg class="decor" width="682" height="480" viewBox="0 0 682 480">
    <g class="ring-large">
      <circle cx="62" cy="60" r="56" fill="var(--ring-dark)"/>
      <path d="M10 60 A52 52 0 0 0 62 112" fill="none" stroke="var(--accent-teal)" stroke-width="12"/>
      <circle cx="62" cy="60" r="28" fill="var(--gear-navy)"/>
    </g>
    <g class="ring-small">
      <circle cx="179" cy="63" r="42" fill="var(--ring-dark)"/>
      <path d="M142 63 A37 37 0 0 0 179 100" fill="none" stroke="var(--accent-teal)" stroke-width="9"/>
      <circle cx="179" cy="58" r="22" fill="var(--brand-green)"/>
      <circle cx="179" cy="58" r="8" fill="var(--ring-dark)"/>
    </g>
    <g class="ring-bottom-left">
      <circle cx="492" cy="432" r="40" fill="var(--ring-dark)"/>
      <path d="M457 432 A35 35 0 0 0 492 467" fill="none" stroke="var(--accent-teal)" stroke-width="9"/>
      <circle cx="492" cy="432" r="22" fill="var(--gear-navy)"/>
    </g>
    <g class="ring-bottom-right">
      <circle cx="607" cy="420" r="58" fill="var(--ring-dark)"/>
      <path d="M557 420 A50 50 0 0 0 607 470" fill="none" stroke="var(--accent-teal)" stroke-width="14"/>
      <circle cx="607" cy="420" r="32" fill="#8a8a8a"/>
      <circle cx="607" cy="420" r="10" fill="var(--ring-dark)"/>
    </g>
  </svg>

  <div class="back-brand">
    <div class="brand-square"></div>
    <div class="brand-name">HARROW<br>IRONWORKS</div>
  </div>

  <div class="invite-heading">
    <span class="arrow left"></span>
    <h1>INVITATION</h1>
    <span class="arrow right"></span>
  </div>

  <ul class="event-details">
    <li>- Date: Fri Aug 26</li>
    <li>- Location: 5678 Road title</li>
    <li>- Time: 6:00pm</li>
    <li>- "Join us to celebrate the Official Opening of Harrow Ironworks"</li>
    <li>- Light dinner provided</li>
  </ul>
</section>

</body>
</html>
```